MAPLEWREN HOUSE DECOR

We need a web design for a new business based in Bonny Hills (NSW). We are a small retail outlet on the Mid North Coast (NSW, Australia) selling home wares, gifts, beach wear, artwork, and hampers etc. We would like to a few different samples if that's not too much trouble (e.g. black and white vs colour, e.g. "beach colours").
We would like the website to communicate that we are an affordable, local (community based) business, with customer satisfaction at the forefront of our mind. We have a strong customer service focus, and in addition to retail sales we are now looking to expand into the online hamper business.
We are open 7 days (except public holidays).
Note: We like the design / layout of the "Lamp Crest 'N' Shelf Website" if you would like to compare www.lampcrestnshelf.com.au

```html
<!DOCTYPE html>
<html lang="en">
<head>
<meta charset="utf-8">
<title>Maplewren House Decor</title>
<link href="https://fonts.googleapis.com/css2?family=Jost:wght@300;400;500;600;700&family=Playfair+Display:ital,wght@1,700&display=swap" rel="stylesheet">
<style>
:root{
  --ink:#262626;
  --bar:#232323;
  --accent:#13b5ea;
  --orange:#f7941d;
  --linen:#e6e1d7;
  --white:#ffffff;
  --text:#333333;
  --muted:#555555;
}
*{margin:0;padding:0;box-sizing:border-box}
html,body{width:1163px;height:1200px;overflow:hidden}
body{position:relative;font-family:'Jost',sans-serif;color:var(--text);background:var(--linen)}
.abs{position:absolute}
a{color:inherit;text-decoration:none}

.topbar{left:0;top:0;width:1163px;height:42px;background:var(--bar);color:#eee;font-size:12px}
.shipping{left:177px;top:13px;display:flex;align-items:center;gap:8px}
.utility{right:0;top:8px;display:flex;align-items:center;font-size:12px}
.utility .sep{margin:0 12px;color:#999}
.signin{background:var(--orange);color:#fff;padding:4px 12px;margin-left:10px;text-transform:uppercase}
.register{margin:0 190px 0 8px;text-transform:uppercase}

.header{left:0;top:42px;width:1163px;height:71px;background:var(--white)}
.logo{left:178px;top:25px;display:flex;align-items:center;gap:8px;color:var(--accent);font-weight:700;font-size:16px;letter-spacing:.5px;white-space:nowrap}
.logo .mark{width:11px;height:11px;background:var(--accent)}
.nav{left:491px;top:28px;display:flex;gap:31px;font-size:12px;font-weight:600;color:var(--text);text-transform:uppercase}
.nav .current{color:var(--accent)}

.panel{left:178px;top:147px;width:806px;height:938px;background:var(--white);box-shadow:0 6px 22px rgba(0,0,0,.25)}

.hero-photo{left:191px;top:168px;width:500px;height:452px;background:linear-gradient(135deg,#9d8f84,#6e5a4d 45%,#c9c3bd)}
.hero-side{left:691px;top:168px;width:279px;height:399px;background:#2c2c2c}
.dots{left:891px;top:189px;display:flex;gap:7px}
.dots span{display:block;width:12px;height:12px;border:2px solid #fff;border-radius:50%}
.dots span.on{border-color:var(--accent)}
.hero-title{left:710px;top:330px;line-height:.9;text-transform:uppercase}
.hero-title .first{color:var(--accent);font-weight:300;font-size:41px;letter-spacing:1px}
.hero-title .line{color:#fff;font-weight:600;font-size:62px;display:block;margin-top:4px}
.shop-now{left:691px;top:567px;width:279px;height:53px;background:var(--accent);color:#fff;font-weight:600;font-size:19px;display:flex;align-items:center;justify-content:center}

.section-title{left:178px;top:648px;width:806px;text-align:center;font-weight:300;font-size:31px;color:#3a3a3a}

.tile{overflow:hidden}
.tile .caption{position:absolute;left:0;right:0;top:58px;height:68px;background:rgba(20,20,20,.82);color:#fff;text-align:center}
.tile .caption h3{font-weight:300;font-size:26px;margin-top:8px;text-transform:uppercase}
.cta{font-family:'Playfair Display',serif;font-style:italic;font-weight:700;font-size:13px}
.wide .caption{left:33px;right:auto;top:60px;width:176px;height:61px;text-align:left;padding-left:15px;background:rgba(60,50,45,.75)}
.wide .caption h3{font-size:25px;margin-top:5px}

.footer{left:0;top:1115px;width:1163px;height:85px;background:var(--bar);color:#ddd}
.footer-row{left:174px;top:22px;display:flex;align-items:center;font-size:12px;font-weight:600}
.footer-label{color:var(--accent)}
.icon-set{display:flex;gap:8px}
.icon-set span{width:13px;height:13px;background:#ccc}
.card-set{display:flex;gap:3px}
.card-set span{width:20px;height:13px;background:#ccc}
.news-input{width:206px;height:21px;background:#3a3a3a;color:#ccc;font-weight:400;font-size:10px;padding:4px 6px}
.news-btn{height:21px;background:var(--accent);color:#fff;font-weight:400;font-size:11px;padding:3px 5px}
.copyright{left:0;top:55px;width:1163px;text-align:center;font-size:14px}
</style>
</head>
<body>

<div class="abs topbar">
  <div class="abs shipping">
    <svg width="15" height="11" viewBox="0 0 15 11"><rect x="0" y="1" width="9" height="7" fill="#13b5ea"/><path d="M9 3h3l3 3v2H9z" fill="#13b5ea"/><circle cx="3" cy="9" r="1.8" fill="#13b5ea"/><circle cx="12" cy="9" r="1.8" fill="#13b5ea"/></svg>
    Free Shipping On Orders Over $200
  </div>
  <div class="abs utility">
    <a href="#">Shopping Cart</a><span class="sep">|</span>
    <a href="#">Checkout</a><span class="sep">|</span>
    <a href="#">Track Order</a>
    <a class="signin" href="#">Sign In</a>
    <a class="register" href="#">Register</a>
  </div>
</div>

<header class="abs header">
  <div class="abs logo"><span class="mark"></span>MAPLEWREN HOUSE DECOR</div>
  <nav class="abs nav">
    <a class="current" href="#">Home</a>
    <a href="#">About Us</a>
    <a href="#">Products</a>
    <a href="#">FAQ'S</a>
    <a href="#">Testimoinials</a>
    <a href="#">Contact Us</a>
  </nav>
</header>

<main class="abs panel"></main>

<div class="abs hero-photo" role="img" aria-label="Store interior with shelves of home wares, cushions, bags and cookware"></div>
<div class="abs hero-side" role="img" aria-label="Darkened view of store shelving behind the shop name"></div>
<div class="abs dots"><span class="on"></span><span></span><span></span><span></span></div>
<h1 class="abs hero-title">
  <span class="first">MAPLEWREN</span>
  <span class="line">HOUSE</span>
  <span class="line">DECOR</span>
</h1>
<a class="abs shop-now" href="#">SHOP NOW</a>

<h2 class="abs section-title">WHAT WE SELL</h2>

<div class="abs tile" style="left:191px;top:706px;width:243px;height:166px;background:linear-gradient(180deg,#b8b2aa,#d9d0c2 60%,#a7754a)" role="img" aria-label="Shelves stacked with colourful cushions and home wares">
  <div class="caption"><h3>Home Wares</h3><div class="cta">Shop Now &gt;</div></div>
</div>
<div class="abs tile" style="left:459px;top:706px;width:244px;height:166px;background:linear-gradient(180deg,#a99d8f,#c9b8a0 55%,#7d8f6a)" role="img" aria-label="Painted artwork and ceramic plates on display">
  <div class="caption"><h3>Artwork</h3><div class="cta">Shop Now &gt;</div></div>
</div>
<div class="abs tile" style="left:728px;top:706px;width:243px;height:166px;background:linear-gradient(180deg,#bdb7ae,#d8d1c4 60%,#c9a46a)" role="img" aria-label="Store display shelving with beach wear and accessories">
  <div class="caption"><h3>Beach Wear</h3><div class="cta">Shop Now &gt;</div></div>
</div>

<div class="abs tile wide" style="left:191px;top:892px;width:390px;height:184px;background:linear-gradient(120deg,#7a5a3c,#d9c29a 50%,#e8dcc4)" role="img" aria-label="Gift box wrapped in gold paper with a brown ribbon bow">
  <div class="caption"><h3>Gifts</h3><div class="cta">Shop Now &gt;</div></div>
</div>
<div class="abs tile wide" style="left:581px;top:892px;width:389px;height:184px;background:linear-gradient(180deg,#d7d7d9,#c8c6c4 55%,#8a6a48)" role="img" aria-label="Wicker hamper basket wrapped in cellophane with a ribbon">
  <div class="caption"><h3>Hampers</h3><div class="cta">Shop Now &gt;</div></div>
</div>

<footer class="abs footer">
  <div class="abs footer-row">
    <span class="footer-label" style="margin-right:16px">FOLLOW US</span>
    <span class="icon-set" style="margin-right:25px"><span></span><span></span><span></span><span></span><span></span></span>
    <span class="footer-label" style="margin-right:12px">PAYMENT</span>
    <span class="card-set" style="margin-right:32px"><span></span><span></span><span></span><span></span><span></span></span>
    <span class="footer-label" style="margin-right:7px">SIGN UP NEWSLETTER</span>
    <span class="news-input">E-mail Newsletter</span>
    <span class="news-btn">SUBSCRIBE</span>
  </div>
  <div class="abs copyright">© Company Name ® Pty Ltd 2014 | Privacy | Terms &amp; Conditions | Sitemap</div>
</footer>

</body>
</html>
```